Website Design for a "Talent Recruitment Agency"

We are looking for a website design for the website of our "Talent Recruitment Agency"; which is called "Crestline Circle".
Our recruitment website "Crestline Circle" will be focusing on: "Crestline Circle: Bridging People & Employers in Switzerland"; which means our target audience is two-folded:
(i) TALENT - that is currently residing in- or outside of Switzerland, and is open for and interested in the "Swiss Job Market".
(ii) COMPANIES - that are looking for talent for specific job vacancies in Switzerland.
With our "Crestline Circle" approach we inted to focus on Membership & Partnership:
(a)"Membership"(TALENT)
and
(b)"Partnership"(COMPANIES)
Some of the competitor sites we like are:
• www.brimlo42.dk
• www.qazet.ch
• www.plovik.ch/en
A sitemap example of our website is attached.
Also attached is a "Crestline Circle" logo in .eps format and one in .jpeg format.
We very much look forward to receive your creative ideas.
Best regards,
Crestline Circle
Crestline Circle: Bridging People & Employers in Switzerland.
Website: crestlinecircle.ch - Twitter: CrestlineCircleCH
Target Market(s)
(i) TALENT (with around 0-10 years of working experience), currently residing in- or outside of Switzerland, but eligible to work in Switzerland.
(ii) COMPANIES (national or international) that are based in Switzerland.
Industry/Entity Type
Recruitment

```html
<!DOCTYPE html>
<html lang="en">
<head>
<meta charset="utf-8">
<title>Crestline Circle</title>
<link href="https://fonts.googleapis.com/css2?family=Arimo:wght@400;700&display=swap" rel="stylesheet">
<style>
  :root {
    --brand-blue: #0a84d8;
    --brand-orange: #ff6428;
    --hero-top: #e3e9ed;
    --hero-bottom: #cfdae2;
    --hero-peak: #b9c6cf;
    --nav-text: #666666;
    --white: #ffffff;
    --footer-bg: #161616;
    --footer-text: #7a7a7a;
    --footer-rule: #2e2e2e;
    --social-a: #3b5998;
    --social-b: #4aa3df;
    --social-c: #1278b8;
    --icon-sky: #a8d4e6;
    --icon-teal: #2f6b7c;
    --icon-navy: #2e4453;
  }
  * { margin: 0; padding: 0; box-sizing: border-box; }
  html, body { width: 1200px; height: 900px; overflow: hidden; }
  body { position: relative; font-family: "Arimo", Arial, sans-serif; background: var(--white); }

  .hero {
    position: absolute; left: 0; top: 0; width: 1200px; height: 347px;
    background:
      radial-gradient(ellipse 260px 240px at 800px 200px, var(--hero-peak), transparent 70%),
      linear-gradient(180deg, var(--hero-top), var(--hero-bottom));
  }
  .site-nav {
    position: absolute; left: 242px; top: 0; width: 692px; height: 32px;
    background: var(--white); display: flex; align-items: center;
  }
  .nav-brand {
    position: absolute; left: 88px; top: 12px; display: flex; align-items: center; gap: 4px;
    font-size: 10px; font-weight: 700; color: var(--brand-blue);
  }
  .nav-brand .dot { width: 10px; height: 10px; border-radius: 50%; background: var(--brand-orange); }
  .nav-links { list-style: none; }
  .nav-links li {
    position: absolute; top: 13px; font-size: 10px; color: var(--nav-text);
  }

  .hero-brand {
    position: absolute; left: 331px; top: 110px; width: 300px;
  }
  .hero-brand .mark {
    width: 80px; height: 80px; border-radius: 50%; background: var(--brand-blue);
    margin-left: 36px; margin-bottom: 4px;
  }
  .hero-brand .name {
    font-size: 29px; font-weight: 700; color: var(--brand-blue); letter-spacing: -0.3px; line-height: 1;
  }
  .tagline {
    margin-top: 10px; font-size: 12.5px; line-height: 13px; color: var(--brand-blue);
  }
  .tagline strong { color: var(--brand-orange); }
  .cta {
    position: absolute; left: 679px; top: 205px; width: 164px; height: 48px;
    background: var(--brand-blue); color: var(--white);
    font-size: 20px; font-weight: 700; display: flex; align-items: center; justify-content: center;
    text-decoration: none;
  }

  .services {
    position: absolute; left: 0; top: 347px; width: 1200px; height: 346px;
    background: var(--brand-orange);
  }
  .service { position: absolute; top: 74px; width: 160px; color: var(--white); }
  .service .art {
    width: 82px; height: 82px; border-radius: 50%; margin: 0 auto;
  }
  .service h2 {
    margin-top: 21px; text-align: center; font-size: 12.5px; font-weight: 700;
  }
  .service p {
    margin-top: 13px; font-size: 7.3px; line-height: 13px;
  }
  .service p strong { font-weight: 700; }

  .site-footer {
    position: absolute; left: 0; top: 693px; width: 1200px; height: 207px;
    background: var(--footer-bg); border-top: 1px solid #3a3a3a;
  }
  .social { position: absolute; top: 111px; width: 28px; height: 28px; }
  .rule { position: absolute; top: 60px; width: 1px; height: 124px; background: var(--footer-rule); }
  .footer-links { list-style: none; position: absolute; font-size: 7.5px; color: var(--footer-text); }
  .footer-links li { height: 15.6px; }
</style>
</head>
<body>

<header class="hero">
  <div role="img" aria-label="Faint photograph of a snowy Swiss mountain peak" style="position:absolute;inset:0;"></div>

  <nav class="site-nav">
    <div class="nav-brand"><span class="dot"></span>Crestline Circle</div>
    <ul class="nav-links">
      <li style="left:256px">Home</li>
      <li style="left:303px">About</li>
      <li style="left:349px">Talent</li>
      <li style="left:396px">Companies</li>
      <li style="left:473px">Jobs</li>
      <li style="left:520px">Events</li>
      <li style="left:567px">Contact</li>
    </ul>
  </nav>

  <div class="hero-brand">
    <div class="mark"></div>
    <div class="name">Crestline Circle</div>
    <p class="tagline">Connecting <strong>Companies</strong> with <strong>Talent</strong> and the<br>other way around</p>
  </div>

  <a class="cta" href="#">Get Started</a>
</header>

<section class="services">
  <article class="service" style="left:315px">
    <div class="art" role="img" aria-label="Illustration of a chick hatching from an egg" style="background:linear-gradient(180deg,var(--icon-sky) 45%,#7cb342 45%)"></div>
    <h2>Recruitment</h2>
    <p style="margin-left:15px;width:160px">"Crestline Circle" is a recruitment agency focusing on: "Crestline Circle: Bridging People &amp; Employers in Switzerland" we connect talent with companies and companies with talent</p>
  </article>

  <article class="service" style="left:507px">
    <div class="art" role="img" aria-label="Illustration of a paint bucket with a brush" style="background:var(--icon-teal)"></div>
    <h2>Talent</h2>
    <p style="margin-left:18px;width:140px">Talent currently residing in- or outside of Switzerland, and is open for and interested in the "Swiss Job Market", and talent will calified as a <strong>Mebership</strong></p>
  </article>

  <article class="service" style="left:688px">
    <div class="art" role="img" aria-label="Illustration of a rocket launching among stars" style="background:var(--icon-navy)"></div>
    <h2>Companies</h2>
    <p style="margin-left:18px;width:140px">Companies that are looking for talent for specific job vacancies in Switzerland, companies should a <strong>Partnership</strong> with crestline circle</p>
  </article>
</section>

<footer class="site-footer">
  <span class="social" style="left:331px;background:var(--social-a)" aria-label="Social profile"></span>
  <span class="social" style="left:391px;background:var(--social-b)" aria-label="Social profile"></span>
  <span class="social" style="left:449px;background:var(--social-c)" aria-label="Social profile"></span>

  <span class="rule" style="left:498px"></span>
  <ul class="footer-links" style="left:571px;top:63px">
    <li>Home</li><li>About</li><li>Talent</li><li>Companies</li><li>Jobs</li><li>Events</li><li>Contact</li>
  </ul>
  <span class="rule" style="left:670px"></span>
  <ul class="footer-links" style="left:723px;top:61px">
    <li>Terms and Conditions</li><li>Disclaimer</li>
  </ul>
</footer>

</body>
</html>
```